PowerPoint presentation

Please clean up this presentation using the overall look of Brovane's brand. www.brovanereit.com. Looking for clean, contemporary, easy to read.

This presentation will be sent to customers to educate them about resources available to them for cost and energy savings.

```html
<!DOCTYPE html>
<html lang="en">
<head>
<meta charset="utf-8">
<title>Brovane E-Playbook – Slide Overview</title>
<link rel="stylesheet" href="https://fonts.googleapis.com/css2?family=Fira+Sans:wght@300;400;600;700&display=swap">
<style>
:root{
  --canvas:#f1f2f1;
  --navy:#24387a;
  --navy-deep:#1b2a63;
  --blue:#2f6bdc;
  --mid:#4f72b6;
  --sky:#8fb9ea;
  --pale:#d4e3f4;
  --ink:#2a3b6e;
  --text:#3b4252;
  --white:#ffffff;
  --ph:#e4e6eb;
  --ph-icon:#9db7dc;
}
*{box-sizing:border-box;margin:0;padding:0}
html,body{width:1200px;height:1200px;overflow:hidden;background:var(--canvas)}
body{position:relative;font-family:'Fira Sans',sans-serif}
.defs{position:absolute;width:0;height:0}
.slide{position:absolute;width:266px;height:200px;background:var(--white);overflow:hidden;color:var(--text)}
.bg{position:absolute;inset:0;width:100%;height:100%}
.stripe{fill:none;stroke:var(--blue);stroke-width:4}
.stripe-thin{fill:none;stroke:var(--sky);stroke-width:1.4}
.abs{position:absolute}
.brand{position:absolute;font-weight:700;color:var(--navy);letter-spacing:.2px;line-height:1}
.brand-light{color:var(--white)}
.foot{position:absolute;left:17px;top:160px;color:var(--white);line-height:1}
.foot .draft{font-size:3.6px;letter-spacing:.2px;display:block;margin-bottom:2px}
.foot .title{font-size:10.5px;font-weight:600;display:block}
.foot .sub{font-size:13px;font-weight:300;display:block;margin-top:1px}
.h{font-weight:400;color:var(--ink);line-height:1.15}
.h-lg{font-size:8.5px}
.h-md{font-size:7.8px}
.body{font-size:4.8px;line-height:1.45;color:var(--text)}
.name{font-size:4.8px;font-weight:600;color:var(--ink)}
.ph{position:absolute;width:41px;height:55px;background:var(--ph);display:flex;align-items:center;justify-content:center}
.ph svg{width:20px;height:20px}
.portrait{position:absolute;width:36px;height:48px;background:linear-gradient(180deg,#e9ecef,#c9ced6 60%,#3d4350)}
.list-item{position:absolute;left:148px;width:112px;font-size:3.6px;line-height:1.35}
.diamond{position:absolute;left:130px;width:9px;height:9px;transform:rotate(45deg)}
.vendor{position:absolute;font-size:4.8px;font-weight:600;color:var(--ink);white-space:nowrap}
.bullets{font-size:3.7px;line-height:1.35;color:var(--text)}
.bullets ul{padding-left:5px}
.chart-label{position:absolute;font-size:2.8px;color:var(--text);white-space:nowrap}
.level-desc{position:absolute;left:167px;width:95px;font-size:3.2px;line-height:1.3}
</style>
</head>
<body>

<svg class="defs" aria-hidden="true">
  <defs>
    <linearGradient id="hands" x1="0" y1="0" x2="1" y2="1">
      <stop offset="0" stop-color="#2a3f86"/>
      <stop offset=".6" stop-color="#3b4f91"/>
      <stop offset="1" stop-color="#22357a"/>
    </linearGradient>
    <linearGradient id="couple" x1="0" y1="0" x2="1" y2="1">
      <stop offset="0" stop-color="#3a4b86"/>
      <stop offset=".5" stop-color="#5a6598"/>
      <stop offset="1" stop-color="#24387a"/>
    </linearGradient>
    <linearGradient id="network" x1="0" y1="0" x2="1" y2="1">
      <stop offset="0" stop-color="#2e4a95"/>
      <stop offset="1" stop-color="#1f3276"/>
    </linearGradient>
  </defs>
</svg>

<!-- Row 1 -->
<section class="slide" style="left:47px;top:160px">
  <svg class="bg" viewBox="0 0 266 200" preserveAspectRatio="none" role="img" aria-label="Photo of a smiling senior couple in a navy tint">
    <polygon points="0,0 260,0 120,126 204,200 0,200" fill="url(#couple)"/>
    <polyline points="268,-2 128,126 212,202" class="stripe"/>
    <polyline points="276,-2 136,126 220,202" class="stripe-thin"/>
  </svg>
  <p class="brand" style="left:148px;top:120px;font-size:13px">Brovane</p>
  <div class="foot" style="left:76px;top:162px">
    <span class="draft">DRAFT 2.7.25</span>
    <span class="title" style="font-size:13px">E-Playbook</span>
  </div>
</section>

<section class="slide" style="left:328px;top:160px">
  <svg class="bg" viewBox="0 0 266 200" preserveAspectRatio="none" role="img" aria-label="Navy panel with faded photo of joined hands">
    <polygon points="0,0 68,0 14,56 156,200 0,200" fill="url(#hands)"/>
    <polyline points="74,0 20,56 162,200" class="stripe"/>
    <polyline points="80,0 26,56 168,200" class="stripe-thin"/>
  </svg>
  <p class="brand brand-light" style="left:30px;top:62px;font-size:9px">Brovane</p>
  <div class="abs" style="left:87px;top:13px;width:168px">
    <p class="h" style="font-size:7.4px;line-height:1.4">The E-Playbook purpose is to operationalize Brovane’s commitment to supporting our tenant operators’ efficient and sustainable practices.</p>
    <p class="body" style="font-size:4.6px;line-height:1.4;margin-top:4px">Working with our Operators, Third-Party Advisors, and Preferred Vendors, Brovane has established consistent and comprehensive practices and approaches that can be replicated and scaled, including:</p>
  </div>
  <svg class="abs" style="left:128px;top:77px;width:100px;height:100px" viewBox="0 0 100 100" aria-hidden="true">
    <g transform="rotate(-90 50 50)" fill="none" stroke-width="22">
      <circle cx="50" cy="50" r="36" stroke="#1f3a8f" stroke-dasharray="37 189.2" stroke-dashoffset="0"/>
      <circle cx="50" cy="50" r="36" stroke="#4b6cb0" stroke-dasharray="37 189.2" stroke-dashoffset="-37.7"/>
      <circle cx="50" cy="50" r="36" stroke="#7ea8df" stroke-dasharray="37 189.2" stroke-dashoffset="-75.4"/>
      <circle cx="50" cy="50" r="36" stroke="#a9c9ec" stroke-dasharray="37 189.2" stroke-dashoffset="-113.1"/>
      <circle cx="50" cy="50" r="36" stroke="#c3d8f1" stroke-dasharray="37 189.2" stroke-dashoffset="-150.8"/>
      <circle cx="50" cy="50" r="36" stroke="#dae6f5" stroke-dasharray="37 189.2" stroke-dashoffset="-188.5"/>
    </g>
    <circle cx="50" cy="50" r="24" fill="#fff"/>
    <text x="50" y="52" text-anchor="middle" font-family="Fira Sans, sans-serif" font-size="7" font-weight="700" fill="#24387a">Brovane</text>
  </svg>
  <div class="foot" style="top:168px"><span class="draft">DRAFT 2.7.25</span><span class="title">E-Playbook</span></div>
</section>

<section class="slide" style="left:607px;top:160px">
  <svg class="bg" viewBox="0 0 266 200" preserveAspectRatio="none" role="img" aria-label="Navy panel with faded photo of joined hands">
    <polygon points="0,0 68,0 14,56 156,200 0,200" fill="url(#hands)"/>
    <polyline points="74,0 20,56 162,200" class="stripe"/>
    <polyline points="80,0 26,56 168,200" class="stripe-thin"/>
  </svg>
  <svg class="abs" style="left:26px;top:51px;width:90px;height:90px" viewBox="0 0 90 90" aria-hidden="true">
    <g transform="rotate(-90 45 45)" fill="none" stroke-width="20">
      <circle cx="45" cy="45" r="33" stroke="#1f3a8f" stroke-dasharray="34 173.3" stroke-dashoffset="0"/>
      <circle cx="45" cy="45" r="33" stroke="#4b6cb0" stroke-dasharray="34 173.3" stroke-dashoffset="-34.55"/>
      <circle cx="45" cy="45" r="33" stroke="#7ea8df" stroke-dasharray="34 173.3" stroke-dashoffset="-69.1"/>
      <circle cx="45" cy="45" r="33" stroke="#a9c9ec" stroke-dasharray="34 173.3" stroke-dashoffset="-103.65"/>
      <circle cx="45" cy="45" r="33" stroke="#c3d8f1" stroke-dasharray="34 173.3" stroke-dashoffset="-138.2"/>
      <circle cx="45" cy="45" r="33" stroke="#dae6f5" stroke-dasharray="34 173.3" stroke-dashoffset="-172.75"/>
    </g>
    <circle cx="45" cy="45" r="22" fill="#fff"/>
    <text x="45" y="47" text-anchor="middle" font-family="Fira Sans, sans-serif" font-size="6.5" font-weight="700" fill="#24387a">Brovane</text>
  </svg>
  <span class="diamond" style="top:34px;background:#1f3a8f"></span>
  <p class="list-item" style="top:35px">Practical and holistic whole-building approach to energy and water efficiency opportunities.</p>
  <span class="diamond" style="top:55px;background:#4b6cb0"></span>
  <p class="list-item" style="top:52px">Knowledgeable and vetted third-party advisors and vendors with technical expertise and proven experience in the senior living and care space, REIT structure, and Brovane.</p>
  <span class="diamond" style="top:81px;background:#6f97d4"></span>
  <p class="list-item" style="top:81px">Responsive and collaborative services from upfront advice to project assessment and solutions to project support and management.</p>
  <span class="diamond" style="top:105px;background:#8cb3e3"></span>
  <p class="list-item" style="top:104px">Best practices, including established and innovative new technologies, implemented successfully across other senior living and care properties and organizations.</p>
  <span class="diamond" style="top:132px;background:#a9c9ec"></span>
  <p class="list-item" style="top:133px">Access to rebates, incentives, and financing from Brovane and other third parties.</p>
  <span class="diamond" style="top:150px;background:#c9dcf1"></span>
  <p class="list-item" style="top:150px">Awareness and support around evolving benchmarking and other regulatory compliance.</p>
  <div class="foot" style="top:176px"><span class="draft">DRAFT 2.7.25</span><span class="title" style="font-size:6.5px">E-Playbook</span></div>
</section>

<section class="slide" style="left:890px;top:160px">
  <svg class="bg" viewBox="0 0 266 200" preserveAspectRatio="none" role="img" aria-label="Navy panel with faded photo of joined hands">
    <polygon points="0,0 68,0 14,56 152,200 0,200" fill="url(#hands)"/>
    <polyline points="74,0 20,56 158,200" class="stripe"/>
    <polyline points="80,0 26,56 164,200" class="stripe-thin"/>
  </svg>
  <p class="brand brand-light" style="left:30px;top:62px;font-size:9px">Brovane</p>
  <p class="h abs" style="left:87px;top:34px;font-size:14px">Collaborative team</p>
  <p class="body abs" style="left:87px;top:67px;width:160px;font-size:6.4px;line-height:1.4">Brovane provides a collaborative team that knows the opportunities and challenges of efficient and sustainable practices as well as the nuances of senior living and care.</p>
  <div class="foot" style="top:159px"><span class="draft">DRAFT 2.7.25</span><span class="title">E-Playbook</span><span class="sub">Team</span></div>
</section>

<!-- Row 2 -->
<section class="slide" style="left:47px;top:389px">
  <svg class="bg" viewBox="0 0 266 200" preserveAspectRatio="none" role="img" aria-label="Navy panel with faded photo of joined hands">
    <polygon points="0,0 68,0 14,56 152,200 0,200" fill="url(#hands)"/>
    <polyline points="74,0 20,56 158,200" class="stripe"/>
    <polyline points="80,0 26,56 164,200" class="stripe-thin"/>
  </svg>
  <p class="brand brand-light" style="left:30px;top:62px;font-size:9px">Brovane</p>
  <p class="h h-lg abs" style="left:143px;top:14px">Brovane Management:</p>
  <div class="abs" style="left:147px;top:53px"><p class="body">Sustainability</p><p class="name" style="margin-top:4px">Lena Marsh</p></div>
  <div class="portrait" style="left:201px;top:37px" role="img" aria-label="Portrait photo of Lena Marsh"></div>
  <div class="abs" style="left:145px;top:98px"><p class="body">Facilities and</p><p class="body" style="margin-top:3px">Capital Projects</p><p class="name" style="margin-top:3px">Paul Ortega</p></div>
  <div class="portrait" style="left:201px;top:88px" role="img" aria-label="Portrait photo of Paul Ortega"></div>
  <div class="abs" style="left:147px;top:156px"><p class="body">Asset Management</p><p class="name" style="margin-top:4px">Joan Whitfield</p></div>
  <div class="portrait" style="left:201px;top:139px" role="img" aria-label="Portrait photo of Joan Whitfield"></div>
  <div class="foot" style="top:161px"><span class="draft">DRAFT 2.7.25</span><span class="title">E-Playbook</span><span class="sub">Team</span></div>
</section>

<section class="slide" style="left:328px;top:389px">
  <svg class="bg" viewBox="0 0 266 200" preserveAspectRatio="none" role="img" aria-label="Navy panel with faded photo of joined hands">
    <polygon points="0,0 68,0 14,56 152,200 0,200" fill="url(#hands)"/>
    <polyline points="74,0 20,56 158,200" class="stripe"/>
    <polyline points="80,0 26,56 164,200" class="stripe-thin"/>
  </svg>
  <p class="brand brand-light" style="left:30px;top:62px;font-size:9px">Brovane</p>
  <p class="h h-lg abs" style="left:98px;top:23px">Program Advisor:</p>
  <p class="body abs" style="left:98px;top:45px">Harrowin E-Advisory</p>
  <p class="name abs" style="left:98px;top:56px">Glen Aldous</p>
  <p class="body abs" style="left:98px;top:67px;width:96px">over 30 years of senior real estate expertise, providing a broad range of sustainability practices, leadership, and access to a preferred vendor network, including technical advisors</p>
  <div class="ph" style="left:201px;top:44px"><svg viewBox="0 0 20 20" aria-hidden="true"><circle cx="10" cy="7" r="3.6" fill="none" stroke="var(--ph-icon)" stroke-width="1.1"/><path d="M3.5 17c0-3.6 2.9-5.6 6.5-5.6s6.5 2 6.5 5.6z" fill="none" stroke="var(--ph-icon)" stroke-width="1.1"/></svg></div>
  <div class="foot" style="top:161px"><span class="draft">DRAFT 2.7.25</span><span class="title">E-Playbook</span><span class="sub">Team</span></div>
</section>

<section class="slide" style="left:607px;top:389px">
  <svg class="bg" viewBox="0 0 266 200" preserveAspectRatio="none" role="img" aria-label="Navy panel with faded photo of joined hands">
    <polygon points="0,0 68,0 14,56 152,200 0,200" fill="url(#hands)"/>
    <polyline points="74,0 20,56 158,200" class="stripe"/>
    <polyline points="80,0 26,56 164,200" class="stripe-thin"/>
  </svg>
  <p class="brand brand-light" style="left:30px;top:62px;font-size:9px">Brovane</p>
  <p class="h h-lg abs" style="left:95px;top:13px">Technical Advisors:</p>
  <p class="body abs" style="left:95px;top:26px;width:160px;line-height:1.35">trusted and seasoned advisors with engagement and domain expertise across the prop-tech, health-tech, benchmarking, and renewable sectors of senior living and care</p>
  <p class="h h-md abs" style="left:94px;top:67px">Skyverant E-3 Partners:</p>
  <p class="body abs" style="left:94px;top:81px;width:112px"><b class="name">Mark Deller</b> and <b class="name">Victor Hale</b>, providing ongoing advice and consultation to owners and operators. Helped implement over $3.5 million of Lighting, Water, and HVAC projects for Healthcare REITs over the last two years.</p>
  <div class="ph" style="left:210px;top:57px"><svg viewBox="0 0 20 20" aria-hidden="true"><circle cx="10" cy="7" r="3.6" fill="none" stroke="var(--ph-icon)" stroke-width="1.1"/><path d="M3.5 17c0-3.6 2.9-5.6 6.5-5.6s6.5 2 6.5 5.6z" fill="none" stroke="var(--ph-icon)" stroke-width="1.1"/></svg></div>
  <p class="name abs" style="left:210px;top:114px">Mark Deller</p>
  <div class="ph" style="left:210px;top:125px"><svg viewBox="0 0 20 20" aria-hidden="true"><circle cx="10" cy="7" r="3.6" fill="none" stroke="var(--ph-icon)" stroke-width="1.1"/><path d="M3.5 17c0-3.6 2.9-5.6 6.5-5.6s6.5 2 6.5 5.6z" fill="none" stroke="var(--ph-icon)" stroke-width="1.1"/></svg></div>
  <p class="name abs" style="left:214px;top:182px">Victor Hale</p>
  <div class="foot" style="top:159px"><span class="draft">DRAFT 2.7.25</span><span class="title">E-Playbook</span><span class="sub">Team</span></div>
</section>

<section class="slide" style="left:890px;top:389px">
  <svg class="bg" viewBox="0 0 266 200" preserveAspectRatio="none" role="img" aria-label="Navy panel with faded photo of joined hands">
    <polygon points="0,0 68,0 14,56 152,200 0,200" fill="url(#hands)"/>
    <polyline points="74,0 20,56 158,200" class="stripe"/>
    <polyline points="80,0 26,56 164,200" class="stripe-thin"/>
  </svg>
  <p class="brand brand-light" style="left:30px;top:62px;font-size:9px">Brovane</p>
  <p class="h h-lg abs" style="left:95px;top:13px">Technical Advisors:</p>
  <p class="h h-lg abs" style="left:96px;top:33px">Serelune Health Advisory Services:</p>
  <p class="name abs" style="left:97px;top:57px">Nora Castel</p>
  <p class="body abs" style="left:97px;top:68px;width:102px">former Chief Clinical Officer at Dawnmere Senior Living, 30-year experience improving quality and business results through strategic planning, innovation, and application of health-tech solutions, including fall management and continuous vital sign monitoring.</p>
  <div class="ph" style="left:210px;top:57px"><svg viewBox="0 0 20 20" aria-hidden="true"><circle cx="10" cy="7" r="3.6" fill="none" stroke="var(--ph-icon)" stroke-width="1.1"/><path d="M3.5 17c0-3.6 2.9-5.6 6.5-5.6s6.5 2 6.5 5.6z" fill="none" stroke="var(--ph-icon)" stroke-width="1.1"/></svg></div>
  <div class="foot" style="top:156px"><span class="draft">DRAFT 2.7.25</span><span class="title">E-Playbook</span><span class="sub">Team</span></div>
</section>

<!-- Row 3 -->
<section class="slide" style="left:47px;top:618px">
  <svg class="bg" viewBox="0 0 266 200" preserveAspectRatio="none" role="img" aria-label="Navy panel with faded photo of joined hands">
    <polygon points="0,0 68,0 14,56 152,200 0,200" fill="url(#hands)"/>
    <polyline points="74,0 20,56 158,200" class="stripe"/>
    <polyline points="80,0 26,56 164,200" class="stripe-thin"/>
  </svg>
  <p class="brand brand-light" style="left:30px;top:62px;font-size:9px">Brovane</p>
  <p class="h h-lg abs" style="left:94px;top:13px">Technical Advisors:</p>
  <p class="h h-lg abs" style="left:95px;top:33px">Verdonique:</p>
  <p class="name abs" style="left:97px;top:57px">Ilse Varga</p>
  <p class="body abs" style="left:97px;top:69px;width:108px">team includes Certified Energy Auditors (CEA), Certified Energy Managers (CEM), and energy and water Data Analysts. They provide utility collection, verification, ESPM integration, Benchmarking, and energy audits for owners and operators.</p>
  <div class="ph" style="left:210px;top:58px"><svg viewBox="0 0 20 20" aria-hidden="true"><circle cx="10" cy="7" r="3.6" fill="none" stroke="var(--ph-icon)" stroke-width="1.1"/><path d="M3.5 17c0-3.6 2.9-5.6 6.5-5.6s6.5 2 6.5 5.6z" fill="none" stroke="var(--ph-icon)" stroke-width="1.1"/></svg></div>
  <div class="foot" style="left:13px;top:158px"><span class="draft">DRAFT 2.7.25</span><span class="title">E-Playbook</span><span class="sub">Team</span></div>
</section>

<section class="slide" style="left:328px;top:618px">
  <svg class="bg" viewBox="0 0 266 200" preserveAspectRatio="none" role="img" aria-label="Navy panel with faded photo of joined hands">
    <polygon points="0,0 68,0 14,56 152,200 0,200" fill="url(#hands)"/>
    <polyline points="74,0 20,56 158,200" class="stripe"/>
    <polyline points="80,0 26,56 164,200" class="stripe-thin"/>
  </svg>
  <p class="brand brand-light" style="left:30px;top:62px;font-size:9px">Brovane</p>
  <p class="h h-lg abs" style="left:95px;top:13px">Technical Advisors:</p>
  <p class="h h-lg abs" style="left:95px;top:33px">Sunquorra:</p>
  <p class="name abs" style="left:97px;top:58px">Drew Tanner</p>
  <p class="body abs" style="left:97px;top:69px;width:104px">former CFO/CPA with 20 years of real estate and solar experience, helping owners and operators evaluate the pros and cons of solar applications.</p>
  <div class="ph" style="left:210px;top:58px"><svg viewBox="0 0 20 20" aria-hidden="true"><circle cx="10" cy="7" r="3.6" fill="none" stroke="var(--ph-icon)" stroke-width="1.1"/><path d="M3.5 17c0-3.6 2.9-5.6 6.5-5.6s6.5 2 6.5 5.6z" fill="none" stroke="var(--ph-icon)" stroke-width="1.1"/></svg></div>
  <div class="foot" style="left:16px;top:158px"><span class="draft">DRAFT 2.7.25</span><span class="title">E-Playbook</span><span class="sub">Team</span></div>
</section>

<section class="slide" style="left:607px;top:618px">
  <svg class="bg" viewBox="0 0 266 200" preserveAspectRatio="none" role="img" aria-label="Navy photo of an open hand beneath a network of people icons">
    <polygon points="0,0 132,0 72,56 212,200 0,200" fill="url(#network)"/>
    <polyline points="138,0 78,56 218,200" class="stripe"/>
    <polyline points="144,0 84,56 224,200" class="stripe-thin"/>
  </svg>
  <p class="brand brand-light" style="left:88px;top:62px;font-size:9px">Brovane</p>
  <p class="h h-lg abs" style="left:154px;top:49px">Preferred Vendors:</p>
  <p class="body abs" style="left:156px;top:69px;width:98px">over 25 preferred and vetted vendors actively engaged and providing services across the senior living and care sector, ranging from energy and water efficiency to utility rebates and financing to rooftop and community solar</p>
  <div class="foot" style="top:158px"><span class="draft">DRAFT 2.7.25</span><span class="title">E-Playbook</span><span class="sub" style="font-size:9px;margin-top:2px">Preferred Vendors:</span></div>
</section>

<section class="slide" style="left:890px;top:618px">
  <svg class="bg" viewBox="0 0 266 200" preserveAspectRatio="none" role="img" aria-label="Navy panel with faded photo of people icons">
    <polygon points="0,0 68,0 14,56 136,200 0,200" fill="url(#network)"/>
    <polyline points="74,0 20,56 142,200" class="stripe"/>
    <polyline points="80,0 26,56 148,200" class="stripe-thin"/>
  </svg>
  <p class="brand brand-light" style="left:30px;top:62px;font-size:9px">Brovane</p>
  <p class="vendor" style="left:134px;top:20px">Ventiquel</p>
  <p class="vendor" style="left:178px;top:20px">Alderquist</p>
  <p class="vendor" style="left:222px;top:20px">Voltessa</p>
  <p class="vendor" style="left:82px;top:43px">Aquavelle</p>
  <p class="vendor" style="left:134px;top:43px">Skyverant</p>
  <p class="vendor" style="left:178px;top:43px">Pontavia</p>
  <p class="vendor" style="left:222px;top:43px">Metrovine</p>
  <p class="vendor" style="left:82px;top:66px">Thermavik</p>
  <p class="vendor" style="left:134px;top:66px">Climquor</p>
  <p class="vendor" style="left:178px;top:66px">Supplivo</p>
  <p class="vendor" style="left:222px;top:66px">Flowquell</p>
  <p class="vendor" style="left:78px;top:88px">Verdonique</p>
  <p class="vendor" style="left:132px;top:88px">Rainvessa</p>
  <p class="vendor" style="left:178px;top:88px">Kovelline</p>
  <p class="vendor" style="left:226px;top:88px">NEVQ</p>
  <p class="vendor" style="left:90px;top:111px">Gridvane</p>
  <p class="vendor" style="left:126px;top:111px">Peakwren HVAC</p>
  <p class="vendor" style="left:178px;top:111px">Staywrell</p>
  <p class="vendor" style="left:222px;top:111px">Seelvant</p>
  <p class="vendor" style="left:130px;top:132px">Sunquorra</p>
  <p class="vendor" style="left:178px;top:132px">Tunovia</p>
  <p class="vendor" style="left:222px;top:132px">Fernquill</p>
  <p class="vendor" style="left:130px;top:158px">Cubrelle</p>
  <p class="vendor" style="left:176px;top:158px">Habivo Lab</p>
  <p class="vendor" style="left:220px;top:158px">Zandrix Vital</p>
  <div class="foot" style="left:12px;top:155px"><span class="draft">DRAFT 2.7.25</span><span class="title">E-Playbook</span><span class="sub" style="font-size:9px;margin-top:2px">Preferred Vendors:</span></div>
</section>

<!-- Row 4 -->
<section class="slide" style="left:47px;top:851px">
  <svg class="bg" viewBox="0 0 266 200" preserveAspectRatio="none" aria-hidden="true">
    <polygon points="0,0 86,0 0,86" fill="#8fc0e8"/>
    <polygon points="0,0 40,0 0,40" fill="#a9d0ef"/>
    <polygon points="0,106 30,106 96,200 0,200" fill="var(--navy)"/>
    <polyline points="36,106 102,200" class="stripe"/>
    <polygon points="146,48 266,48 266,74 134.1,74" fill="#22377a"/>
    <polygon points="134.1,74 266,74 266,99 122.7,99" fill="#34529a"/>
    <polygon points="122.7,99 266,99 266,124 111.3,124" fill="#5a86c8"/>
    <polygon points="111.3,124 266,124 266,149 99.9,149" fill="#8ab6e2"/>
    <polygon points="99.9,149 266,149 266,175 88,175" fill="#b7d3ee"/>
    <g font-family="Fira Sans, sans-serif" font-weight="700" font-size="5" text-anchor="middle">
      <rect x="65" y="54" width="19" height="11" rx="2" fill="#22377a"/><text x="74.5" y="61.5" fill="#fff">50%</text>
      <rect x="65" y="78" width="19" height="11" rx="2" fill="#34529a"/><text x="74.5" y="85.5" fill="#fff">40%</text>
      <rect x="65" y="103" width="19" height="11" rx="2" fill="#5a86c8"/><text x="74.5" y="110.5" fill="#fff">30%</text>
      <rect x="65" y="128" width="19" height="11" rx="2" fill="#8ab6e2"/><text x="74.5" y="135.5" fill="#24387a">20%</text>
      <rect x="65" y="158" width="19" height="11" rx="2" fill="#d6e6f5"/><text x="74.5" y="165.5" fill="#24387a">10%</text>
    </g>
    <g font-family="Fira Sans, sans-serif" font-weight="600" font-size="5">
      <text x="145" y="63.5" fill="#fff">5</text>
      <text x="137" y="88.5" fill="#fff">Level 4</text>
      <text x="127" y="113.5" fill="#fff">Level 3</text>
      <text x="115" y="138.5" fill="#24387a">Level 2</text>
      <text x="103" y="164.5" fill="#24387a">Level 1</text>
    </g>
  </svg>
  <p class="brand" style="left:6px;top:90px;font-size:7px">Brovane</p>
  <p class="h h-lg abs" style="left:73px;top:17px">Multi-Level Approach to Building Efficiency</p>
  <p class="body abs" style="left:63px;top:34px;font-size:5.4px">Energy and Water Savings Potential</p>
  <p class="level-desc" style="top:53px;color:#fff"><b>5. Smart</b> whole building strategy including Solar, Battery Storage and EV charging stations</p>
  <p class="level-desc" style="top:77px;color:#fff"><b>4. Efficient</b> capital replacement strategy including HVAC, Mechanicals, Building envelope and Roofing</p>
  <p class="level-desc" style="top:102px;color:#fff"><b>3. Enhanced</b> HVAC maintenance, insulation, and efficiency technology such as Smart Thermostats, Smart Motors and Chips</p>
  <p class="level-desc" style="top:129px;color:var(--ink)"><b>2. Practical</b> whole building technology such as Water Efficiency Valves and Power Grid Filters</p>
  <p class="level-desc" style="top:153px;color:var(--ink)"><b>1. Initial</b> LED lighting and Water Efficiency Improvements such as low flow plumbing fixtures, smart irrigation &amp; landscape</p>
  <div class="foot" style="left:8px;top:178px"><span class="draft">DRAFT 2.7.25</span><span class="title" style="font-size:6.5px">E-Playbook</span></div>
</section>

<section class="slide" style="left:328px;top:851px">
  <svg class="bg" viewBox="0 0 266 200" preserveAspectRatio="none" aria-hidden="true">
    <polygon points="0,0 36,0 0,36" fill="var(--navy)"/>
    <polyline points="42,0 0,42" class="stripe"/>
    <polygon points="0,62 8,62 120,200 0,200" fill="#86bde6"/>
    <polyline points="12,62 124,200" class="stripe"/>
  </svg>
  <p class="brand" style="left:6px;top:44px;font-size:8px">Brovane</p>
  <p class="h h-lg abs" style="left:69px;top:8px">E-Playbook - 80/20 Energy Efficiency Rule</p>
  <div class="bullets abs" style="left:73px;top:26px;width:182px">
    <p><b>In Senior Living &amp; Care, HVAC, Lighting, and Water Heating typically accounts for up to 80% of energy use*:</b></p>
    <ul>
      <li>Electricity uses include: 18% lighting, 1% water heating, 18% ventilation, 15% space cooling, 5% space heating, 20% miscellaneous, 2% computing, 9% office equipment, 9% refrigeration, and 3% cooking.</li>
      <li>Natural gas uses include: 46% water heating, 46% space heating, 2% miscellaneous, and 6% cooking.</li>
    </ul>
  </div>
  <p class="body abs" style="left:69px;top:82px;font-size:5.4px">Electricity End Uses</p>
  <svg class="abs" style="left:154px;top:90px;width:80px;height:80px" viewBox="0 0 80 80" aria-hidden="true">
    <g transform="rotate(-90 40 40)" fill="none" stroke-width="18">
      <circle cx="40" cy="40" r="29" stroke="#24387a" stroke-dasharray="9.11 182.2" stroke-dashoffset="0"/>
      <circle cx="40" cy="40" r="29" stroke="#a9c9ec" stroke-dasharray="27.33 182.2" stroke-dashoffset="-9.11"/>
      <circle cx="40" cy="40" r="29" stroke="#4b6cb0" stroke-dasharray="32.8 182.2" stroke-dashoffset="-36.44"/>
      <circle cx="40" cy="40" r="29" stroke="#8cb3e3" stroke-dasharray="1.82 182.2" stroke-dashoffset="-69.24"/>
      <circle cx="40" cy="40" r="29" stroke="#24387a" stroke-dasharray="32.8 182.2" stroke-dashoffset="-71.06"/>
      <circle cx="40" cy="40" r="29" stroke="#1e3c9a" stroke-dasharray="5.47 182.2" stroke-dashoffset="-103.85"/>
      <circle cx="40" cy="40" r="29" stroke="#8cb3e3" stroke-dasharray="16.4 182.2" stroke-dashoffset="-109.32"/>
      <circle cx="40" cy="40" r="29" stroke="#6f97d4" stroke-dasharray="16.4 182.2" stroke-dashoffset="-125.72"/>
      <circle cx="40" cy="40" r="29" stroke="#1e3c9a" stroke-dasharray="3.64 182.2" stroke-dashoffset="-142.12"/>
      <circle cx="40" cy="40" r="29" stroke="#4f72b6" stroke-dasharray="36.44 182.2" stroke-dashoffset="-145.76"/>
    </g>
    <circle cx="40" cy="40" r="19" fill="#fff"/>
    <text x="40" y="41.5" text-anchor="middle" font-family="Fira Sans, sans-serif" font-size="3.8" font-weight="700" fill="#24387a">Midvessa Energy</text>
  </svg>
  <p class="chart-label" style="left:222px;top:82px">Space Heating 5%</p>
  <p class="chart-label" style="left:222px;top:96px">Space Cooling 15%</p>
  <p class="chart-label" style="left:234px;top:130px">Ventilation 18%</p>
  <p class="chart-label" style="left:230px;top:152px">Water Heating 1%</p>
  <p class="chart-label" style="left:220px;top:166px">Lighting 18%</p>
  <p class="chart-label" style="left:140px;top:171px">3% Cooking</p>
  <p class="chart-label" style="left:118px;top:153px">9% Refrigeration</p>
  <p class="chart-label" style="left:106px;top:128px">9% Office Equipment</p>
  <p class="chart-label" style="left:109px;top:113px">2% Computing</p>
  <p class="chart-label" style="left:108px;top:96px">20% Miscellaneous</p>
  <p class="chart-label" style="left:218px;top:181px;text-align:right;line-height:1.3">*Average EUI for Nursing<br>Homes in the Midwest</p>
  <div class="foot" style="left:10px;top:148px"><span class="draft">DRAFT 2.7.25</span><span class="title">E-Playbook</span><span class="sub" style="font-size:8.5px;margin-top:3px">80/20 Energy</span><span class="sub" style="font-size:8.5px;margin-top:3px">Efficiency Rule</span></div>
</section>

<section class="slide" style="left:607px;top:851px">
  <svg class="bg" viewBox="0 0 266 200" preserveAspectRatio="none" aria-hidden="true">
    <polygon points="0,0 36,0 0,36" fill="var(--navy)"/>
    <polyline points="42,0 0,42" class="stripe"/>
    <polygon points="0,62 8,62 120,200 0,200" fill="#86bde6"/>
    <polyline points="12,62 124,200" class="stripe"/>
  </svg>
  <p class="brand" style="left:6px;top:44px;font-size:8px">Brovane</p>
  <p class="h h-lg abs" style="left:70px;top:8px">E-Playbook - 80/20 Energy Efficiency Rule</p>
  <div class="bullets abs" style="left:70px;top:25px;width:188px;font-size:3.2px">
    <p><b>HVAC Lesson Learned:</b></p>
    <ul>
      <li>Single largest equipment investment at most properties, often over $1million+</li>
      <li>Up to 60% of total energy cost</li>
      <li>It is not just the upfront or replacement cost but the total cost of ownership, including maintenance, preservation, and efficiency</li>
      <li>Proper maintenance is a critical component to overall efficiency, preservation, and ownership cost</li>
      <li>You need to stay on top of issues and plan ahead</li>
      <li>If you make a mistake, you will have to live with it for the next 15 years (less if you don’t maintain it)</li>
      <li>Operators need to be both Care and Real Estate focused</li>
    </ul>
  </div>
  <p class="body abs" style="left:70px;top:86px;font-size:5.4px">Natural Gas End Uses</p>
  <svg class="abs" style="left:144px;top:95px;width:90px;height:90px" viewBox="0 0 90 90" aria-hidden="true">
    <g transform="rotate(-90 45 45)" fill="none" stroke-width="22">
      <circle cx="45" cy="45" r="33" stroke="#8fa4c9" stroke-dasharray="4.15 207.35" stroke-dashoffset="0"/>
      <circle cx="45" cy="45" r="33" stroke="#24387a" stroke-dasharray="95.38 207.35" stroke-dashoffset="-4.15"/>
      <circle cx="45" cy="45" r="33" stroke="#d0e1f3" stroke-dasharray="95.38 207.35" stroke-dashoffset="-99.53"/>
      <circle cx="45" cy="45" r="33" stroke="#1e3c9a" stroke-dasharray="12.44 207.35" stroke-dashoffset="-194.91"/>
    </g>
    <circle cx="45" cy="45" r="21" fill="#fff"/>
    <text x="45" y="46.5" text-anchor="middle" font-family="Fira Sans, sans-serif" font-size="4" font-weight="700" fill="#24387a">Midvessa Energy</text>
  </svg>
  <p class="chart-label" style="left:216px;top:92px">Miscellaneous 2%</p>
  <p class="chart-label" style="left:228px;top:109px">Space Heating 46%</p>
  <p class="chart-label" style="left:110px;top:150px">46% Water Heating</p>
  <p class="chart-label" style="left:124px;top:100px">6% Cooking</p>
  <p class="chart-label" style="left:218px;top:181px;text-align:right;line-height:1.3">*Average EUI for Nursing<br>Homes in the Midwest</p>
  <div class="foot" style="left:10px;top:148px"><span class="draft">DRAFT 2.7.25</span><span class="title">E-Playbook</span><span class="sub" style="font-size:8.5px;margin-top:3px">80/20 Energy</span><span class="sub" style="font-size:8.5px;margin-top:3px">Efficiency Rule</span></div>
</section>

<section class="slide" style="left:890px;top:851px">
  <svg class="bg" viewBox="0 0 266 200" preserveAspectRatio="none" role="img" aria-label="Navy photo of scattered puzzle pieces and question marks">
    <polygon points="0,0 222,0 98,118 166,200 0,200" fill="url(#hands)"/>
    <polyline points="228,0 104,118 172,200" class="stripe"/>
    <polyline points="234,0 110,118 178,200" class="stripe-thin"/>
  </svg>
  <p class="brand" style="left:120px;top:116px;font-size:12px">Brovane</p>
  <p class="h abs" style="left:148px;top:81px;font-size:9.5px">Let’s Have A Discussion</p>
  <div class="foot" style="left:11px;top:172px"><span class="draft">DRAFT 2.7.25</span><span class="title">E-Playbook</span></div>
</section>

</body>
</html>
```